依頼概要
■依頼の目的/概要
大型施設の共有スペースに展示する商品のPOPのデザインをお願いします。
展示の全体イメージがありますのでそれに合わせたイメージで制作して下さい。

■依頼詳細
大型SC内の新店舗の商品展示用のPOPになります。
展示イメージに合うようにPOPの制作をして下さい。
前回の展示のPOPを参考にアップしておきますが、同じような配置にする必要はございません。
前回は背景色などは変えずに、商品名、金額等を、レディース、メンズ、キッズの三種類に色分けして区別しておりました。
今回はキッズはないのですが、レディース、メンズ、雑貨と別れておりますので、うまく区別できるような工夫をお願いします。
サイズは A4縦サイズ。
店舗によって商品、金額、アイテム数は変化するので、変更できるような仕様にして下さい。
フォントはモリサワでしたら入っております。
採用後は使用フォントを納品データと共にお知らせください。

■重視する点
Illustrator・Photoshopの経験必須でお願いします。
新店舗のPOPになりますので、」お客様の目に留まるようなデザインが望ましいです。

■継続依頼について
弊社ではこういった案件が多くあり、次回は母の日、父の日等もありますので、継続的依頼できるありがたいです。

その他何かご不明な点がございましたら、お気軽にご質問下さい。
よろしくお願いいたします。
参考用イメージをアップします。

今回の展示イメージ
前回のPOPイメージ

の2点です。
1店舗の最大アイテム数は6になります。
前回のPOP参考例はあくまで参考です。
同じように作作らなくても良いので参考程度にして頂ければ幸いです。
展示イメージにある通り、POPは各マネキン、雑貨の前に置くものになります。
新店舗のオープンなのでワクワクするようなイメージで制作してもらえればと思います。
集まりが少ないので当選額を上乗せします。
それに伴い期間も延長いたします。
ご応募いただきありがとうございました。

見やすくイメージに沿っていたため。

たくさんのご参加ありがとうございました。
ぜひ次回もご参加下さい。

```html
<!DOCTYPE html>
<html lang="ja">
<head>
<meta charset="utf-8">
<title>POP</title>
<link href="https://fonts.googleapis.com/css2?family=M+PLUS+Rounded+1c:wght@800;900&family=Noto+Sans+JP:wght@500;700;900&family=Noto+Serif+JP:wght@900&display=swap" rel="stylesheet">
<style>
:root{
  --cream:#fff8dc;
  --cream-deep:#fde9a6;
  --orange:#f08a12;
  --orange-deep:#e06a00;
  --white:#ffffff;
  --ink:#3a2a1a;
  --price:#9b1b1b;
  --grey:#a8a8a8;
  --pink-bg:#fbd3d8;  --pink-band:#e8424f;
  --gold-bg:#fde07a;  --gold-band:#ee8a1a;
  --green-bg:#b6dc6a; --green-band:#4e9a2a;
  --blue-bg:#bfe3f5;  --blue-band:#2f8fcf;
  --amber-bg:#fbb45a; --amber-band:#e86d10;
  --lilac-bg:#ddc6ee; --lilac-band:#8e5fb8;
}
*{margin:0;padding:0;box-sizing:border-box}
html,body{width:846px;height:1200px;overflow:hidden}
body{font-family:"Noto Sans JP",sans-serif;color:var(--ink)}
.poster{position:relative;width:846px;height:1200px;overflow:hidden;
  background:radial-gradient(circle at 20% 22%,#fffdf0 0,var(--cream) 40%,var(--cream-deep) 100%)}
.header{position:absolute;left:0;top:0;width:846px;height:108px;
  background:linear-gradient(var(--orange),var(--orange-deep));
  display:flex;align-items:center;justify-content:center}
.store-name{color:var(--white);font-weight:900;font-size:50px;letter-spacing:4px}
.store-logo{position:absolute;left:16px;top:14px;width:84px;height:32px;background:var(--white);
  border:2px solid var(--orange-deep);font-size:15px;font-weight:700;display:flex;align-items:center;justify-content:center}
.limited{position:absolute;right:14px;top:44px;width:104px;height:104px;border-radius:50%;
  background:var(--orange);border:4px solid var(--white);color:var(--white);
  font-weight:900;font-size:24px;line-height:1.15;display:flex;flex-direction:column;align-items:center;justify-content:center}
.title{position:absolute;left:0;width:846px;top:118px;text-align:center;
  font-family:"Noto Serif JP",serif;font-weight:900;font-size:118px;line-height:1;font-style:italic;
  color:var(--orange);
  text-shadow:4px 4px 0 var(--white),-4px -4px 0 var(--white),4px -4px 0 var(--white),-4px 4px 0 var(--white),0 6px 0 var(--white),6px 8px 6px rgba(160,80,0,.35)}
.appeal{position:absolute;right:96px;top:258px;font-size:16px;font-weight:700;color:var(--orange-deep)}
.grid{position:absolute;left:24px;top:282px;display:grid;grid-template-columns:392px 392px;column-gap:16px;row-gap:18px}
.card{position:relative;width:392px;height:272px;overflow:hidden;border:3px solid var(--white)}
.card .label{position:absolute;left:14px;top:6px;font-family:"M PLUS Rounded 1c",sans-serif;font-weight:900;font-size:50px;letter-spacing:1px;
  text-shadow:2px 2px 0 var(--white),-2px -2px 0 var(--white),2px -2px 0 var(--white),-2px 2px 0 var(--white)}
.label .c1{color:#e84a9a}.label .c2{color:#f5a000}.label .c3{color:#58b52a}.label .c4{color:#27a0dc}.label .c5{color:#e84a9a}
.card .image{position:absolute;left:60px;top:58px;width:272px;height:152px}
.card .image span{position:absolute;left:0;top:0;width:100%;height:100%;display:flex;align-items:center;justify-content:center;font-size:26px;font-weight:500;color:var(--grey)}
.card .band{position:absolute;left:0;bottom:0;width:100%;height:60px;display:flex;align-items:center;justify-content:space-between;padding:0 10px}
.band .cat{color:var(--white);font-weight:900;font-size:22px}
.band .price{background:var(--white);border-radius:6px;padding:0 14px;font-family:"Noto Serif JP",serif;font-weight:900;font-size:46px;line-height:52px;color:var(--price)}
.pink{background:var(--pink-bg)}.pink .band{background:var(--pink-band)}
.gold{background:var(--gold-bg)}.gold .band{background:var(--gold-band)}
.green{background:var(--green-bg)}.green .band{background:var(--green-band)}
.blue{background:var(--blue-bg)}.blue .band{background:var(--blue-band)}
.amber{background:var(--amber-bg)}.amber .band{background:var(--amber-band)}
.lilac{background:var(--lilac-bg)}.lilac .band{background:var(--lilac-band)}
.footer{position:absolute;left:0;bottom:0;width:846px;height:54px;background:linear-gradient(var(--orange),var(--orange-deep));
  color:var(--white);font-weight:900;font-size:28px;letter-spacing:3px;display:flex;align-items:center;justify-content:center}
</style>
</head>
<body>
<main class="poster">
  <header class="header">
    <div class="store-logo">店舗ロゴ</div>
    <h1 class="store-name">店舗名</h1>
  </header>
  <div class="limited"><span>限定</span><span>商品</span></div>
  <h2 class="title">POPタイトル</h2>
  <p class="appeal">アピールコメント</p>

  <section class="grid">
    <article class="card pink">
      <div class="label"><span class="c1">レ</span><span class="c2">デ</span><span class="c3">ィ</span><span class="c4">ー</span><span class="c5">ス</span></div>
      <div class="image"><svg width="272" height="152" viewBox="0 0 272 152" role="img" aria-label="商品写真"><g fill="#fff"><circle cx="60" cy="80" r="52"/><circle cx="120" cy="55" r="52"/><circle cx="180" cy="60" r="50"/><circle cx="220" cy="90" r="48"/><circle cx="140" cy="100" r="50"/><circle cx="80" cy="110" r="40"/></g></svg><span>商品イメージ</span></div>
      <div class="band"><span class="cat">雑貨</span><span class="price">¥5990</span></div>
    </article>
    <article class="card gold">
      <div class="label"><span class="c1">レ</span><span class="c2">デ</span><span class="c3">ィ</span><span class="c4">ー</span><span class="c5">ス</span></div>
      <div class="image"><svg width="272" height="152" viewBox="0 0 272 152" role="img" aria-label="商品写真"><g fill="#fff"><circle cx="60" cy="80" r="52"/><circle cx="120" cy="55" r="52"/><circle cx="180" cy="60" r="50"/><circle cx="220" cy="90" r="48"/><circle cx="140" cy="100" r="50"/><circle cx="80" cy="110" r="40"/></g></svg><span>商品イメージ</span></div>
      <div class="band"><span class="cat">雑貨</span><span class="price">¥5990</span></div>
    </article>
    <article class="card green">
      <div class="label"><span class="c1">レ</span><span class="c2">デ</span><span class="c3">ィ</span><span class="c4">ー</span><span class="c5">ス</span></div>
      <div class="image"><svg width="272" height="152" viewBox="0 0 272 152" role="img" aria-label="商品写真"><g fill="#fff"><circle cx="60" cy="80" r="52"/><circle cx="120" cy="55" r="52"/><circle cx="180" cy="60" r="50"/><circle cx="220" cy="90" r="48"/><circle cx="140" cy="100" r="50"/><circle cx="80" cy="110" r="40"/></g></svg><span>商品イメージ</span></div>
      <div class="band"><span class="cat">雑貨</span><span class="price">¥5990</span></div>
    </article>
    <article class="card blue">
      <div class="label"><span class="c1">レ</span><span class="c2">デ</span><span class="c3">ィ</span><span class="c4">ー</span><span class="c5">ス</span></div>
      <div class="image"><svg width="272" height="152" viewBox="0 0 272 152" role="img" aria-label="商品写真"><g fill="#fff"><circle cx="60" cy="80" r="52"/><circle cx="120" cy="55" r="52"/><circle cx="180" cy="60" r="50"/><circle cx="220" cy="90" r="48"/><circle cx="140" cy="100" r="50"/><circle cx="80" cy="110" r="40"/></g></svg><span>商品イメージ</span></div>
      <div class="band"><span class="cat">雑貨</span><span class="price">¥5990</span></div>
    </article>
    <article class="card amber">
      <div class="label"><span class="c1">レ</span><span class="c2">デ</span><span class="c3">ィ</span><span class="c4">ー</span><span class="c5">ス</span></div>
      <div class="image"><svg width="272" height="152" viewBox="0 0 272 152" role="img" aria-label="商品写真"><g fill="#fff"><circle cx="60" cy="80" r="52"/><circle cx="120" cy="55" r="52"/><circle cx="180" cy="60" r="50"/><circle cx="220" cy="90" r="48"/><circle cx="140" cy="100" r="50"/><circle cx="80" cy="110" r="40"/></g></svg><span>商品イメージ</span></div>
      <div class="band"><span class="cat">雑貨</span><span class="price">¥5990</span></div>
    </article>
    <article class="card lilac">
      <div class="label"><span class="c1">レ</span><span class="c2">デ</span><span class="c3">ィ</span><span class="c4">ー</span><span class="c5">ス</span></div>
      <div class="image"><svg width="272" height="152" viewBox="0 0 272 152" role="img" aria-label="商品写真"><g fill="#fff"><circle cx="60" cy="80" r="52"/><circle cx="120" cy="55" r="52"/><circle cx="180" cy="60" r="50"/><circle cx="220" cy="90" r="48"/><circle cx="140" cy="100" r="50"/><circle cx="80" cy="110" r="40"/></g></svg><span>商品イメージ</span></div>
      <div class="band"><span class="cat">雑貨</span><span class="price">¥5990</span></div>
    </article>
  </section>

  <footer class="footer">コーポレートロゴ</footer>
</main>
</body>
</html>
```